Brightwell Systems, a software development company, needs a website

We need a website to promote our software development company. The company is brand new and we want to market ourselves. We develop all kinds of software from web applications, to desktop applications, to mobile applications. Small company, not a lot of history, just need something flashy.

```html
<!DOCTYPE html>
<html lang="en">
<head>
<meta charset="utf-8">
<title>Brightwell Systems Inc. | Software Development</title>
<link href="https://fonts.googleapis.com/css2?family=Poppins:wght@400;500;600&family=Roboto+Condensed:wght@400&family=Roboto+Slab:wght@400;500&display=swap" rel="stylesheet">
<style>
  :root{
    --navy:#0b1f5c;
    --blue:#1f8ad6;
    --text:#222633;
    --muted:#4a4f5c;
    --line:#d5d9e2;
    --white:#ffffff;
    --faint:#e3e8f2;
  }
  *{box-sizing:border-box;margin:0;padding:0}
  html,body{width:1200px;height:2171px;overflow:hidden;background:var(--white)}
  body{position:relative;font-family:'Poppins',sans-serif;color:var(--text)}
  .abs{position:absolute}

  /* Header */
  .site-header{position:absolute;left:0;top:0;width:1200px;height:82px;background:var(--white)}
  .brand{position:absolute;left:142px;top:16px;font-weight:600;font-size:35px;color:var(--navy);letter-spacing:-.3px}
  .header-phone{position:absolute;left:722px;top:28px;display:flex;align-items:center;gap:10px;font-size:15px;color:var(--blue)}
  .btn{display:flex;align-items:center;justify-content:center;background:var(--navy);color:var(--white);font-family:'Poppins',sans-serif;font-weight:500;text-decoration:none}
  .header-cta{position:absolute;left:861px;top:23px;width:199px;height:33px;font-size:16px}

  /* Hero */
  .hero{position:absolute;left:0;top:82px;width:1200px;height:540px;
    background:linear-gradient(180deg,#f0a34a 0%,#d98a4a 20%,#7d8aa0 45%,#4a5a6e 70%,#1f2c3a 100%)}
  .hero-title{position:absolute;left:0;top:516px;width:1200px;text-align:center;font-family:'Roboto Condensed',sans-serif;font-weight:400;font-size:31px;line-height:48px;color:var(--white)}

  /* About */
  .about-brand{position:absolute;left:140px;top:848px;width:300px;text-align:center;font-weight:600;font-size:21px;color:var(--navy)}
  .about-divider{position:absolute;left:435px;top:713px;width:4px;height:208px;background:var(--navy)}
  .about-arrow{position:absolute;left:439px;top:803px}
  .section-heading{font-weight:400;color:var(--navy)}
  .section-heading .accent{color:var(--blue)}
  .about-heading{position:absolute;left:479px;top:690px;font-size:29px;line-height:34px}
  .about-text{position:absolute;left:479px;top:766px;width:540px;font-size:12.7px;line-height:24.4px;color:var(--text)}
  .about-more{position:absolute;left:482px;top:899px;width:108px;height:38px;font-size:14px}

  /* Services */
  .services-heading{position:absolute;left:0;top:1062px;width:1200px;text-align:center;font-size:32px}
  .services-lead{position:absolute;left:0;top:1110px;width:1200px;text-align:center;font-size:13.5px;color:var(--text)}
  .service{position:absolute;top:1175px;width:290px;text-align:center}
  .service-icon{display:block;margin:0 auto}
  .service-title{margin-top:16px;font-family:'Roboto Slab',serif;font-weight:500;font-size:14.5px;color:var(--text)}
  .service-text{margin-top:8px;font-size:13px;line-height:23px;color:var(--muted)}
  .services-cta{position:absolute;left:498px;top:1440px;width:198px;height:38px;font-size:15.5px}

  /* Map */
  .map{position:absolute;left:0;top:1542px;width:1200px;height:289px;
    background:linear-gradient(135deg,#dfe5ee 0%,#cfd8e4 40%,#e6ebf2 70%,#d4dce7 100%)}
  .map-pin{position:absolute;left:644px;top:1650px}
  .map-card{position:absolute;left:709px;top:1633px;width:191px;height:78px;background:var(--navy);color:var(--white);padding:10px 12px;font-size:12.5px;line-height:19px;box-shadow:2px 3px 6px rgba(0,0,0,.25)}
  .map-card strong{font-weight:500;font-size:13px}
  .map-card::before{content:"";position:absolute;left:-16px;top:6px;border-style:solid;border-width:0 16px 14px 0;border-color:transparent var(--navy) transparent transparent}

  /* Footer (children positioned against the page) */
  .site-footer{position:static}
  .footer-heading{position:absolute;top:1882px;font-size:14px;font-weight:400;color:var(--text)}
  .contact-list{position:absolute;left:140px;top:1920px;list-style:none;font-size:13px;line-height:19px;color:var(--text)}
  .contact-list li{display:flex;gap:13px;margin-bottom:11px}
  .contact-list svg{flex:none;margin-top:2px}
  .abn{position:absolute;left:140px;top:2033px;font-size:14px;color:var(--text)}
  .abn .label{color:var(--blue);font-weight:500}
  .social{position:absolute;left:139px;top:2080px;display:flex;gap:10px}
  .social span{display:block;width:26px;height:26px;border:1.5px solid var(--blue)}
  .footer-brand{position:absolute;left:278px;top:2068px;font-weight:600;font-size:35px;line-height:44px;color:var(--faint)}
  .quick-links{position:absolute;left:505px;top:1918px;list-style:none;font-size:13px;line-height:26.5px}
  .quick-links a{color:var(--text);text-decoration:none}
  .contact-form{position:absolute;left:724px;top:1924px;width:334px;height:190px}
  .field{position:absolute;border:1px solid var(--line);background:var(--white);font-size:12.5px;color:var(--text);padding:6px 8px}
  .submit{position:absolute;left:1px;top:154px;width:125px;height:35px;font-size:16px}
  .bottom-bar{position:absolute;left:0;top:2135px;width:1200px;height:36px;background:var(--navy);color:var(--white);text-align:center;font-size:13px;line-height:36px}
</style>
</head>
<body>

<header class="site-header">
  <div class="brand">Brightwell Systems Inc.</div>
  <div class="header-phone">
    <svg width="18" height="18" viewBox="0 0 24 24" fill="none" stroke="#0b1f5c" stroke-width="1.8"><path d="M5 3h4l2 5-2.5 1.5a11 11 0 0 0 6 6L16 13l5 2v4a2 2 0 0 1-2 2A17 17 0 0 1 3 5a2 2 0 0 1 2-2z"/></svg>
    555.014.2870
  </div>
  <a class="btn header-cta" href="#contact">Get Your Solution Now!</a>
</header>

<section class="hero" role="img" aria-label="Aerial photograph of a city skyline of glass towers at sunset beside a river"></section>
<h1 class="hero-title">We Develop All Kinds Of Software From Web Applications, To Desktop<br>Applications, To Mobile Applications In USA</h1>

<section class="about" id="about">
  <div class="about-brand">Brightwell Systems Inc.</div>
  <div class="about-divider"></div>
  <svg class="about-arrow" width="13" height="24" viewBox="0 0 13 24"><path d="M0 0L13 12L0 24Z" fill="#0b1f5c"/></svg>
  <h2 class="section-heading about-heading">About<br><span class="accent">Our Mission</span></h2>
  <p class="about-text">Lorem ipsum dolor sit amet, consectetuer adipiscing elit, sed diam nonummy nibh euismod tincidunt ut laoreet dolore magna aliquam erat volutpat. Ut wisi enim ad minim veniam, quis nostrud exerci tation ullamcorper suscipit lobortis nisl ut aliquip ex ea commodo consequat. Duis autem vel eum iriure dolor in hendrerit in vulputate velit esse molestie consequat.</p>
  <a class="btn about-more" href="#about">Know More</a>
</section>

<section class="services" id="services">
  <h2 class="section-heading services-heading">Our <span class="accent">Services</span></h2>
  <p class="services-lead">Lorem ipsum dolor sit amet, consectetuer adipiscing elit, sed diam nonummy nibh euismod.</p>

  <article class="service" style="left:131px">
    <svg class="service-icon" width="100" height="110" viewBox="0 0 100 110">
      <ellipse cx="50" cy="104" rx="34" ry="4" fill="#e9ecf1"/>
      <circle cx="50" cy="48" r="46" fill="#f3f4f7" stroke="#0b1f5c" stroke-width="3"/>
      <rect x="30" y="34" width="40" height="27" rx="2" fill="#fff" stroke="#1f8ad6" stroke-width="2.5"/>
      <path d="M25 64h50" stroke="#1f8ad6" stroke-width="3"/>
      <path d="M44 42l-6 5 6 5M56 42l6 5-6 5M52 40l-4 14" stroke="#0b1f5c" stroke-width="2" fill="none"/>
    </svg>
    <h3 class="service-title">Web Applications</h3>
    <p class="service-text">Lorem ipsum dolor sit amet, sectetuer adipiscin ga mortis nisl aliquip fdafe ea commodo consequat. ....[+]</p>
  </article>

  <article class="service" style="left:451px">
    <svg class="service-icon" width="100" height="110" viewBox="0 0 100 110">
      <ellipse cx="50" cy="104" rx="34" ry="4" fill="#e9ecf1"/>
      <circle cx="50" cy="48" r="46" fill="#f3f4f7" stroke="#0b1f5c" stroke-width="3"/>
      <rect x="30" y="31" width="40" height="28" rx="2" fill="#1f8ad6"/>
      <path d="M36 39h20M36 45h28M36 51h16" stroke="#fff" stroke-width="2"/>
      <path d="M50 59v7M40 67h20" stroke="#0b1f5c" stroke-width="3"/>
    </svg>
    <h3 class="service-title">Desktop Applications</h3>
    <p class="service-text">Lorem ipsum dolor sit amet, sectetuer adipiscin ga mortis nisl aliquip fdafe ea commodo consequat. ....[+]</p>
  </article>

  <article class="service" style="left:770px">
    <svg class="service-icon" width="100" height="110" viewBox="0 0 100 110">
      <ellipse cx="50" cy="104" rx="34" ry="4" fill="#e9ecf1"/>
      <circle cx="50" cy="48" r="46" fill="#f3f4f7" stroke="#0b1f5c" stroke-width="3"/>
      <rect x="36" y="26" width="24" height="42" rx="3" fill="#fff" stroke="#1f8ad6" stroke-width="2.5"/>
      <circle cx="48" cy="46" r="6" fill="none" stroke="#0b1f5c" stroke-width="2"/>
      <path d="M62 42h8M62 48h6" stroke="#1f8ad6" stroke-width="2"/>
    </svg>
    <h3 class="service-title">Mobile Applications</h3>
    <p class="service-text">Lorem ipsum dolor sit amet, sectetuer adipiscin ga mortis nisl aliquip fdafe ea commodo consequat. ....[+]</p>
  </article>

  <a class="btn services-cta" href="#contact">Contact Us Today</a>
</section>

<section class="location">
  <div class="map" role="img" aria-label="Regional road map showing the office location"></div>
  <svg class="map-pin" width="24" height="34" viewBox="0 0 24 34"><path d="M12 2a9 9 0 0 0-9 9c0 7 9 17 9 17s9-10 9-17a9 9 0 0 0-9-9z" fill="#e8eef6" stroke="#1f8ad6" stroke-width="2"/><circle cx="12" cy="11" r="3" fill="none" stroke="#1f8ad6" stroke-width="2"/><ellipse cx="12" cy="31" rx="7" ry="2" fill="none" stroke="#1f8ad6" stroke-width="1.5"/></svg>
  <div class="map-card"><strong>Brightwell Systems Inc.</strong><br>Street Name, City Name<br>US,&nbsp; NewYork 123458</div>
</section>

<footer class="site-footer" id="contact">
  <h4 class="footer-heading" style="left:142px">Contact Us</h4>
  <h4 class="footer-heading" style="left:502px">Quick Links</h4>
  <h4 class="footer-heading" style="left:721px">Contact Form</h4>

  <ul class="contact-list">
    <li><svg width="14" height="16" viewBox="0 0 14 18" fill="none" stroke="#1f8ad6" stroke-width="1.6"><path d="M7 1a6 6 0 0 0-6 6c0 5 6 10 6 10s6-5 6-10a6 6 0 0 0-6-6z"/><circle cx="7" cy="7" r="2"/></svg><span>Street Name, City Name<br>US,&nbsp; NewYork 123458</span></li>
    <li><svg width="14" height="14" viewBox="0 0 24 24" fill="none" stroke="#1f8ad6" stroke-width="2"><path d="M5 3h4l2 5-2.5 1.5a11 11 0 0 0 6 6L16 13l5 2v4a2 2 0 0 1-2 2A17 17 0 0 1 3 5a2 2 0 0 1 2-2z"/></svg><span>555.014.2871</span></li>
    <li><svg width="14" height="12" viewBox="0 0 16 12" fill="none" stroke="#1f8ad6" stroke-width="1.5"><rect x="1" y="1" width="14" height="10"/><path d="M1 1l7 6 7-6"/></svg><span>inquiry@brightwellsystems.com</span></li>
  </ul>
  <p class="abn"><span class="label">ABN:</span> 31 208 7719 4402</p>
  <div class="social" aria-label="Social links"><span></span><span></span><span></span></div>
  <div class="footer-brand">Brightwell Systems Inc.</div>

  <ul class="quick-links">
    <li><a href="#">Home</a></li>
    <li><a href="#about">About Us</a></li>
    <li><a href="#services">Services</a></li>
    <li><a href="#team">Team</a></li>
    <li><a href="#contact">Contact Us</a></li>
  </ul>

  <form class="contact-form">
    <div class="field" style="left:0;top:0;width:334px;height:32px">First Name</div>
    <div class="field" style="left:0;top:37px;width:162px;height:34px">Email</div>
    <div class="field" style="left:173px;top:37px;width:161px;height:34px">Phone</div>
    <div class="field" style="left:0;top:74px;width:334px;height:74px">Message</div>
    <div class="btn submit">Submit</div>
  </form>
</footer>

<div class="bottom-bar">Copyright © 2019 Brightwell Systems Inc. All Rights Reserved | Privacy</div>

</body>
</html>
```